Monthly Wall Calendar for German shepherd Rescue

We will provide photo's description of dogs and placement of photos and all written material for calendar. We need a wall calendar and we will need as a final output pdf files with the proper bleed lines to send to printer. We have uploaded what the prior year calendar looked like. We are looking for something similar this year.

Generally there is a large monthly photo and 2-3 smaller ones added to the calendar page.

Target Market(s)

Our supporters and animal rescue people.

Font styles to use
Serif

Colors
6c459b
b7a5cd

Requirements
Must have
• A final pdf file with bleed lines for printer.
Nice to have
• The uploaded calendar gives a nice idea of what we are looking for as well as this link. http://brimleyhaven.com/calendar-2016-photo-spread/ and http://brimleyhaven.com/covers-2017/
Should not have
• Not cluttered

```html
<!DOCTYPE html>
<html lang="en">
<head>
<meta charset="utf-8">
<title>January 2018 Wall Calendar</title>
<link href="https://fonts.googleapis.com/css2?family=Playfair+Display:ital,wght@0,400;0,700;1,400&family=Lato:wght@400;700&display=swap" rel="stylesheet">
<style>
:root{
  --purple:#6c459b;
  --lilac:#b7a5cd;
  --panel:#9474c2;
  --red:#d8232a;
  --ink:#222;
  --grid:#cfcfcf;
  --weekend:#e9e9ec;
  --white:#fff;
  --photo-top:#5a6e3a;
  --photo-mid:#6f8a3e;
  --photo-low:#8aa84a;
}
*{margin:0;padding:0;box-sizing:border-box}
html,body{width:802px;height:1200px;overflow:hidden;background:var(--white)}
.sheet{position:relative;width:802px;height:1200px;overflow:hidden;background:var(--white);font-family:"Lato",sans-serif;color:var(--ink)}
.photo-area{background:linear-gradient(180deg,var(--photo-top) 0%,var(--photo-mid) 55%,var(--photo-low) 100%)}
.hero-photo{position:absolute;left:0;top:0;width:802px;height:520px}
.hanger-hole{position:absolute;left:372px;top:-30px;width:56px;height:56px;border-radius:50%;background:#2b2b2b}
.accent{position:absolute;left:587px;top:400px}
.month-title{position:absolute;left:21px;top:522px;font-family:"Playfair Display",serif;font-style:italic;font-size:54px;line-height:1.2;color:var(--purple);letter-spacing:1px}
.title-rule{position:absolute;left:222px;top:578px;width:128px;height:2px;background:var(--purple)}
.year{position:absolute;left:360px;top:534px;font-family:"Playfair Display",serif;font-size:40px;line-height:1.2;color:var(--ink)}
.grid{position:absolute;left:21px;top:593px;width:562px;border-collapse:collapse;table-layout:fixed;border-top:3px solid var(--purple)}
.grid th{font-family:"Playfair Display",serif;font-weight:700;font-size:20px;text-align:left;padding:4px 6px;height:36px;border-bottom:1px solid var(--grid)}
.grid td{height:63px;vertical-align:top;padding:6px 8px;font-size:24px;font-weight:700;border-bottom:1px solid var(--grid)}
.grid .weekend{background:var(--weekend)}
.grid .holiday{color:var(--red)}
.side-text{position:absolute;left:655px;top:598px;color:var(--white);font-family:"Lato",sans-serif;font-size:40px;line-height:1.25}
.mini{position:absolute;top:948px;width:132px;font-size:8px}
.mini table{border-collapse:collapse;width:100%}
.mini caption{font-size:9px;color:var(--purple);padding-bottom:2px}
.mini th,.mini td{text-align:center;height:11px;font-weight:400}
.mini th{color:var(--purple);font-weight:700}
.mini-dec{left:21px}
.mini-feb{left:166px}
.holidays{position:absolute;left:310px;top:946px;width:272px;font-size:9px;border-top:1px solid var(--grid)}
.holidays h3{text-align:center;color:var(--red);font-family:"Playfair Display",serif;font-size:12px;padding:2px 4px}
.holidays li{list-style:none;padding:1px 0}
.holidays b{color:var(--red);display:inline-block;width:44px}
.thumb{position:absolute;top:1040px;width:289px;height:160px}
.thumb-one{left:0}
.thumb-two{left:293px}
.brand{position:absolute;left:587px;top:1040px;width:215px;height:160px;display:flex;flex-direction:column;align-items:center;justify-content:center;gap:10px}
.brand-mark{display:flex;align-items:center;gap:8px;font-family:"Playfair Display",serif;font-size:22px;color:var(--purple)}
.brand-dot{width:28px;height:28px;border-radius:50%;background:var(--lilac)}
.brand-url{font-family:"Playfair Display",serif;font-size:15px;color:var(--purple)}
</style>
</head>
<body>
<div class="sheet">
  <div class="hero-photo photo-area" role="img" aria-label="Monthly photo: a German shepherd lying on green grass"></div>
  <div class="hanger-hole"></div>

  <svg class="accent" width="215" height="627" viewBox="0 0 215 627" aria-hidden="true">
    <polygon points="0,70 215,8 215,36 0,98" fill="var(--lilac)"/>
    <polygon points="0,98 215,36 215,40 0,102" fill="var(--purple)"/>
    <polygon points="0,122 215,80 215,627 0,627" fill="var(--panel)"/>
  </svg>

  <div class="month-title">January</div>
  <div class="title-rule"></div>
  <div class="year">2018</div>

  <table class="grid">
    <thead><tr><th>Sun</th><th>Mon</th><th>Tue</th><th>Wed</th><th>Thu</th><th>Fri</th><th>Sat</th></tr></thead>
    <tbody>
      <tr><td class="weekend"></td><td class="holiday">1</td><td>2</td><td>3</td><td>4</td><td>5</td><td class="weekend">6</td></tr>
      <tr><td class="weekend">7</td><td>8</td><td>9</td><td>10</td><td>11</td><td>12</td><td class="weekend">13</td></tr>
      <tr><td class="weekend holiday">14</td><td>15</td><td>16</td><td>17</td><td>18</td><td>19</td><td class="weekend">20</td></tr>
      <tr><td class="weekend holiday">21</td><td>22</td><td>23</td><td>24</td><td>25</td><td>26</td><td class="weekend">27</td></tr>
      <tr><td class="weekend">28</td><td>29</td><td>30</td><td class="holiday">31</td><td></td><td></td><td class="weekend"></td></tr>
    </tbody>
  </table>

  <div class="side-text">Your<br>Text<br>here<br>......</div>

  <div class="mini mini-dec"><table>
    <caption>December 2017</caption>
    <tr><th>S</th><th>M</th><th>T</th><th>W</th><th>T</th><th>F</th><th>S</th></tr>
    <tr><td></td><td></td><td></td><td></td><td></td><td>1</td><td>2</td></tr>
    <tr><td>3</td><td>4</td><td>5</td><td>6</td><td>7</td><td>8</td><td>9</td></tr>
    <tr><td>10</td><td>11</td><td>12</td><td>13</td><td>14</td><td>15</td><td>16</td></tr>
    <tr><td>17</td><td>18</td><td>19</td><td>20</td><td>21</td><td>22</td><td>23</td></tr>
    <tr><td>24</td><td>25</td><td>26</td><td>27</td><td>28</td><td>29</td><td>30</td></tr>
    <tr><td>31</td><td></td><td></td><td></td><td></td><td></td><td></td></tr>
  </table></div>

  <div class="mini mini-feb"><table>
    <caption>February 2018</caption>
    <tr><th>S</th><th>M</th><th>T</th><th>W</th><th>T</th><th>F</th><th>S</th></tr>
    <tr><td></td><td></td><td></td><td></td><td>1</td><td>2</td><td>3</td></tr>
    <tr><td>4</td><td>5</td><td>6</td><td>7</td><td>8</td><td>9</td><td>10</td></tr>
    <tr><td>11</td><td>12</td><td>13</td><td>14</td><td>15</td><td>16</td><td>17</td></tr>
    <tr><td>18</td><td>19</td><td>20</td><td>21</td><td>22</td><td>23</td><td>24</td></tr>
    <tr><td>25</td><td>26</td><td>27</td><td>28</td><td></td><td></td><td></td></tr>
  </table></div>

  <div class="holidays">
    <h3>Holidays</h3>
    <ul>
      <li><b>01 Jan</b> New Year's Day</li>
      <li><b>14 Jan</b> Rescue Open House</li>
      <li><b>15 Jan</b> Volunteer Day</li>
      <li><b>31 Jan</b> Adoption Drive</li>
    </ul>
  </div>

  <div class="thumb thumb-one photo-area" role="img" aria-label="Small photo: a German shepherd resting on grass"></div>
  <div class="thumb thumb-two photo-area" role="img" aria-label="Small photo: a German shepherd resting on grass"></div>

  <div class="brand">
    <div class="brand-mark"><span class="brand-dot"></span>Brimley Haven</div>
    <div class="brand-url">www.brimleyhaven.com</div>
  </div>
</div>
</body>
</html>
```